Tidal Hounds Dog Behaviour, Training and Natural Healthcare Business Card Design

I am an experienced and qualified dog behavioural trainer and natural animal healthcare consultant offering a range of services to help pet dog owners with the "whole dog".
COLOURS: A soft light blue in the background - can be fading out or split, red should also feature
LOGO: Dog, healing hands, silhouette, shadow
SERVICES: Behaviour Consults, Training, Complex Skills Coaching Walking Coaching, Diet & Nutrition, Environmental Enrichment, Lifestyle and Lifestage Adaptations, Massage, Natural Health Options
BY LINE: Happy Dogs, Happy Owners
VALUES: Promoting communication and connection between dogs and their owners.
FOCUS: Nutritional guidance and environmental adaptation are often needed to complete the package and increase the success rate of training and behaviour modification.

Target Market(s)

Everyone who has a dog who they wish to improve their relationship with

Industry/Entity Type

Communication

Contact Information for Business Card

Tidal Hounds, Rosalind Vukovic, 0417 286350, tidalhounds7@quellmail.net, www.tidalhounds7.net, Qualified Dog Behavioural Trainer and Natural Animal Healthcare Consultant

Font styles to use
Sans Serif
Script

Colors
85cae6
ec2027

Requirements
Must have
• A clear indication that it is a dog services business. A raised feature
Should not have
• Pawprints, cartoons

Files

```html
<!DOCTYPE html>
<html lang="en">
<head>
<meta charset="utf-8">
<title>Tidal Hounds – Business Card</title>
<link rel="stylesheet" href="https://fonts.googleapis.com/css2?family=Barlow+Semi+Condensed:wght@300;400&family=Krona+One&family=Roboto+Condensed:wght@400&display=swap">
<style>
  :root {
    --paper: #e6e9ea;
    --band: #c8ccda;
    --ink-navy: #17364a;
    --ink-quote: #505357;
    --ink-white: #ffffff;
    --accent-red: #c9695f;
    --footer-bg: #ffffff;
    --footer-ink: #9a9ea4;
  }
  * { margin: 0; padding: 0; box-sizing: border-box; }
  html, body { width: 1200px; height: 720px; overflow: hidden; background: var(--paper); }
  .card {
    position: relative;
    width: 1200px;
    height: 720px;
    background: var(--paper);
    overflow: hidden;
  }
  .card__band { position: absolute; inset: 0; width: 1200px; height: 720px; }

  .focus-quote {
    position: absolute;
    top: 44px;
    left: 86px;
    width: 1000px;
    text-align: center;
    white-space: nowrap;
    font-family: "Barlow Semi Condensed", sans-serif;
    font-weight: 400;
    font-size: 25px;
    line-height: 32px;
    letter-spacing: -0.5px;
    color: var(--ink-quote);
  }
  .quote-mark {
    position: absolute;
    top: 42px;
    left: 998px;
    width: 48px;
    height: 24px;
  }

  .brand__dot {
    position: absolute;
    top: 232px;
    left: 238px;
    width: 100px;
    height: 100px;
    border-radius: 50%;
    background: var(--ink-navy);
  }
  .brand__name {
    position: absolute;
    top: 378px;
    left: 0;
    width: 576px;
    text-align: center;
    font-family: "Krona One", sans-serif;
    font-weight: 400;
    font-size: 37px;
    line-height: 48px;
    letter-spacing: 2.6px;
    color: var(--ink-navy);
    white-space: nowrap;
  }

  .services {
    position: absolute;
    top: 249px;
    left: 582px;
    display: flex;
    font-family: "Barlow Semi Condensed", sans-serif;
    font-weight: 300;
    font-size: 26.5px;
    line-height: 31.3px;
    letter-spacing: -0.7px;
    color: var(--ink-white);
    white-space: nowrap;
  }
  .services__col { list-style: none; }
  .services__col--primary { width: 264px; }

  .values {
    position: absolute;
    top: 540px;
    left: 0;
    width: 1224px;
    text-align: center;
    font-family: "Krona One", sans-serif;
    font-size: 18.6px;
    line-height: 32px;
    letter-spacing: 3.4px;
    color: var(--accent-red);
  }

  .contact {
    position: absolute;
    top: 640px;
    left: 0;
    width: 1200px;
    height: 40px;
    background: var(--footer-bg);
    display: flex;
    align-items: center;
    justify-content: center;
    gap: 44px;
    font-family: "Roboto Condensed", sans-serif;
    font-size: 19px;
    letter-spacing: 1.6px;
    color: var(--footer-ink);
    list-style: none;
    white-space: nowrap;
  }
</style>
</head>
<body>
  <main class="card">
    <svg class="card__band" viewBox="0 0 1200 720" aria-hidden="true">
      <path d="M0 117 C 300 190, 480 212, 640 207 C 860 200, 1040 190, 1200 171 L 1200 500 C 1000 470, 800 455, 600 462 C 380 470, 180 510, 0 555 Z" fill="var(--band)"/>
    </svg>

    <p class="focus-quote">Nutritional guidance and environmental adaptation are often needed to complete the<br>package and increase the success rate of training and behaviour modification.</p>
    <svg class="quote-mark" viewBox="0 0 48 24" aria-hidden="true">
      <path d="M0 2 H17 V13 L11 22 H6 L10 13 H0 Z M28 2 H45 V13 L39 22 H34 L38 13 H28 Z" fill="var(--ink-quote)"/>
    </svg>

    <span class="brand__dot"></span>
    <h1 class="brand__name">Tidal Hounds</h1>

    <div class="services">
      <ul class="services__col services__col--primary">
        <li>Behaviour Consults</li>
        <li>Training</li>
        <li>Complex Skills Coaching</li>
        <li>Walking Coaching</li>
        <li>Diet &amp; Nutrition</li>
      </ul>
      <ul class="services__col">
        <li>Environmental Enrichment</li>
        <li>Lifestyle</li>
        <li>Lifestage Adaptations</li>
        <li>Massage</li>
        <li>Natural Health Options</li>
      </ul>
    </div>

    <p class="values">Promoting communication and connection between<br>dogs and their owners.</p>

    <ul class="contact">
      <li>Tidal Hounds, Rosalind Vukovic</li>
      <li>0417 286350</li>
      <li>tidalhounds7@quellmail.net</li>
      <li>www.tidalhounds7.net</li>
    </ul>
  </main>
</body>
</html>
```